We are working with a new commercial flooring contractor in California. They work on schools, hospitals, and government projects.
A few websites for inspiration:
https://plainrockcoverings.com (These guys are competitors and provide the same work our client does).
https://tjtilework.com (Although NOT a contractor, the simplicity of this site is stunning).
https://www.quietlantern.com (NOT a flooring contractor, but this site is modern, and has a boldness to it).
https://www.sagemeadowatelier.com/en-us (website for an Architectural office that is clean and showcases their work. I can see this working for a flooring contractor).
Thank you for taking the time to consider designing a website for us. We are web developers based in Stockton, CA, USA. Most of our projects go through the same process. Understanding this process may help you win a project with us. We custom-code all of our websites in-house. We don’t have any requirements as to what tools you use for your design, but we ask that you follow these guidelines.
IMAGES:
If you use any images or icons in the design, we ask that you have a link to the asset so we can purchase the image/icon. Most of the designs we submit do not have the customer’s images on them unless they have some great images. Be creative; show us the feeling you are trying to portray with your image choices. Use any royalty-free site you choose. We subscribe to Kestral and mainly use their images, but we can purchase images outside of Kestral.
FONTS:
We ask that you identify the fonts you’re using in the design. This can be done in a message if you want. We typically use Vantor Fonts and Kestral Fonts.
CONTENT:
We're always open to different content and ideas. We often submit designs with stock images so the client can see our vision. We typically take pictures after the website launch to use their images with our vision. Lorem Ipsum is fine for paragraphs, but we ask that you make the Headers with correct English. We want to be able to show the vision and identify the sections of the website.
INSPIRATION:
We typically add a couple of links in the brief of websites we like to help you get started in your design.
REVISIONS:
We do not often ask for revisions of the designs unless we see something in the design that may not appeal to the client. If there are slight changes that we want to make, we do that in the development process.
FEEDBACK:
We rarely give feedback on designs during the design process. We are working on many website projects and do not have the time to provide feedback. We usually respond if your request is well thought out and asks specific questions, but a note asking “feedback, please” usually goes unanswered.

```html
<!DOCTYPE html>
<html lang="en">
<head>
<meta charset="utf-8">
<title>Crestline Floors — Commercial Flooring</title>
<link href="https://fonts.googleapis.com/css2?family=Oswald:wght@500;700&family=Poppins:wght@400;500;600;700&display=swap" rel="stylesheet">
<style>
:root{
  --red:#e4232b;
  --ink:#1b1b1b;
  --text:#555;
  --muted:#8a8a8a;
  --light:#f2f2f2;
  --line:#dcdcdc;
  --dark:#1e1e1e;
  --white:#fff;
  --wood:#a0623a;
  --wood-dark:#4a2a18;
}
*{margin:0;padding:0;box-sizing:border-box}
html,body{width:1200px;height:5092px;overflow:hidden}
body{font-family:"Poppins",sans-serif;color:var(--text);background:var(--white);position:relative}
.section{position:absolute;left:0;width:1200px;overflow:hidden}
.abs{position:absolute}
.btn{display:inline-block;background:var(--red);color:var(--white);font:600 11px "Poppins",sans-serif;letter-spacing:.8px;text-transform:uppercase;padding:12px 24px;border-radius:2px;white-space:nowrap}
.photo{position:absolute}
.h2{font:700 30px/1.2 "Poppins",sans-serif;color:var(--ink)}
.p{font:400 12px/1.75 "Poppins",sans-serif;color:var(--text)}

/* header */
.site-header{top:0;height:72px;background:var(--white);z-index:3;box-shadow:0 2px 8px rgba(0,0,0,.06)}
.main-nav{left:144px;top:28px;display:flex;gap:26px;font:600 11px "Poppins",sans-serif;color:var(--ink);text-transform:uppercase}
.main-nav .active{color:var(--red)}
.brand{left:500px;top:10px;display:flex;align-items:center;gap:10px}
.brand-mark{width:52px;height:52px;border-radius:50%;background:var(--red)}
.brand-name{font:700 16px "Poppins",sans-serif;color:var(--ink);white-space:nowrap}
.call{left:724px;top:20px;display:flex;align-items:center;gap:10px}
.call-icon{width:32px;height:32px;border-radius:50%;background:var(--red);display:flex;align-items:center;justify-content:center}
.call-text small{display:block;font:400 10px "Poppins",sans-serif;color:var(--muted)}
.call-text b{font:600 13px "Poppins",sans-serif;color:var(--ink);white-space:nowrap}
.site-header .btn{position:absolute;left:904px;top:18px}

/* hero */
.hero{top:72px;height:560px;background:linear-gradient(180deg,#2d3440 0%,#3c3a3a 45%,#8a5632 70%,#b77a4a 100%)}
.hero-title{left:0;width:1200px;top:210px;text-align:center;font:700 46px/1.1 "Oswald",sans-serif;color:var(--white);text-transform:uppercase;letter-spacing:.5px}
.hero-list{left:0;width:1200px;top:352px;display:flex;justify-content:center;gap:40px;font:600 13px "Oswald",sans-serif;color:var(--white);letter-spacing:1px}
.hero-list span::before{content:"";display:inline-block;width:8px;height:8px;background:var(--red);border-radius:50%;margin-right:8px;vertical-align:1px}
.hero .btn{position:absolute;left:520px;top:402px}
.hero-dots{left:96px;top:250px;display:flex;flex-direction:column;gap:10px}
.hero-dots i{width:8px;height:8px;border-radius:50%;background:rgba(255,255,255,.5)}
.hero-dots i:first-child{background:var(--red)}

/* about */
.about{top:632px;height:568px;background:var(--white)}
.about-ring{left:112px;top:64px;width:340px;height:340px;border-radius:50%;border:2px solid var(--line)}
.about-photo{left:126px;top:78px;width:312px;height:312px;border-radius:50%;background:radial-gradient(circle at 40% 40%,#c98a55,#8a5232)}
.about-badge{left:324px;top:270px;width:110px;height:110px;border-radius:50%;background:var(--white);border:3px solid var(--red);display:flex;align-items:center;justify-content:center;font:700 12px "Poppins",sans-serif;color:var(--red);text-align:center}
.about-copy{left:608px;top:104px;width:460px}
.about-copy .h2{font-size:22px;margin-bottom:16px}
.ticks{margin-top:18px;display:grid;grid-template-columns:1fr 1fr;gap:12px 20px;font:400 11px "Poppins",sans-serif;color:var(--text)}
.ticks li{list-style:none;display:flex;align-items:center;gap:8px}
.ticks li::before{content:"";width:10px;height:10px;border-radius:50%;background:var(--red);flex:none}
.about-copy .btn{margin-top:28px}

/* services */
.services{top:1200px;height:1060px;background:var(--light)}
.section-head{left:0;width:1200px;top:64px;text-align:center}
.section-head .h2{font-size:22px}
.section-head p{font:400 11px "Poppins",sans-serif;color:var(--muted);margin-top:6px}
.tile-label{position:absolute;font:700 11px "Poppins",sans-serif;color:var(--ink);text-transform:uppercase;text-align:center}
.coat-text{position:absolute;left:420px;top:612px;width:352px;text-align:center;font:400 10px/1.6 "Poppins",sans-serif;color:var(--text)}

/* banner */
.banner{top:2288px;height:200px;background:linear-gradient(90deg,var(--wood-dark),#6b3b22 50%,#3a2012)}
.banner h3{position:absolute;left:144px;top:72px;font:700 22px "Poppins",sans-serif;color:var(--white)}
.banner p{position:absolute;left:144px;top:108px;font:400 11px "Poppins",sans-serif;color:#d8c8bc}
.banner .btn{position:absolute;left:888px;top:78px}

/* projects */
.projects{top:2520px;height:540px;background:var(--white)}
.projects .h2{position:absolute;left:144px;top:72px;font-size:22px}
.projects .btn{position:absolute;left:900px;top:66px}
.proj-label{position:absolute;top:500px;font:600 13px "Poppins",sans-serif;color:var(--ink)}
.proj-arrow{left:124px;top:302px;width:36px;height:36px;background:var(--red);display:flex;align-items:center;justify-content:center}

/* testimonials */
.testimonials{top:3080px;height:520px;background:var(--white);border-top:1px solid #eee}
.testi-copy{left:144px;top:60px;width:400px}
.testi-copy .h2{font-size:24px}
.quote{margin-top:28px;font:700 40px/1 "Oswald",sans-serif;color:var(--red)}
.testi-copy .p{margin-top:10px;font-size:12px}
.person{margin-top:28px;display:flex;align-items:center;gap:14px}
.avatar{width:52px;height:52px;border-radius:50%;background:#c7c0b8}
.person b{display:block;font:600 13px "Poppins",sans-serif;color:var(--ink)}
.person small{font:400 11px "Poppins",sans-serif;color:var(--muted)}
.testi-photo{left:620px;top:0;width:580px;height:480px;background:linear-gradient(160deg,#eae6df,#bdb5aa 60%,#8b8478)}

/* areas */
.areas{top:3600px;height:412px;background:var(--white)}
.map{left:0;top:0;width:640px;height:412px;background:linear-gradient(110deg,#f3f3f3 0%,#e6e6e6 30%,#e98a8d 48%,#e4232b 60%,#ec9a9d 75%,#f3f3f3 100%)}
.areas-copy{left:700px;top:60px;width:380px}
.areas-copy .h2{font-size:22px;text-transform:uppercase}
.areas-copy .p{margin-top:10px;font-size:11px}
.area-list{margin-top:18px}
.area-item{display:flex;align-items:center;gap:14px;margin-bottom:16px}
.area-thumb{width:54px;height:40px;background:linear-gradient(135deg,#6f6a5e,#3b3a33)}
.area-item b{display:block;font:600 11px "Poppins",sans-serif;color:var(--ink);text-transform:uppercase}
.area-item small{font:400 10px "Poppins",sans-serif;color:var(--muted)}

/* contact */
.contact{top:4012px;height:640px;background:linear-gradient(100deg,#8f6a47,#c49c6e 45%,#e1cdb0 70%,#9f8266)}
.contact-card{left:144px;top:28px;width:388px;height:612px;background:var(--white);padding:36px 32px}
.contact-card h3{font:700 22px "Poppins",sans-serif;color:var(--ink);text-align:center}
.contact-card .lead{font:400 10px/1.6 "Poppins",sans-serif;color:var(--muted);text-align:center;margin:10px 0 22px}
.field-row{display:flex;gap:12px;margin-bottom:14px}
.field{flex:1;height:40px;border:1px solid var(--line);font:400 11px "Poppins",sans-serif;color:var(--muted);padding:12px 12px;display:flex;justify-content:space-between}
.field.tall{height:120px}
.contact-card .btn{display:block;width:170px;margin:24px auto 0;text-align:center}

/* footer */
.site-footer{top:4652px;height:440px;background:var(--dark);color:#cfcfcf}
.foot-col{position:absolute;top:68px}
.foot-col h4{font:600 15px "Poppins",sans-serif;color:var(--white);margin-bottom:20px;text-transform:uppercase}
.foot-col li{list-style:none;font:400 12px/1.6 "Poppins",sans-serif;margin-bottom:12px;display:flex;gap:10px}
.foot-col li i{width:10px;height:10px;border-radius:50%;background:var(--red);flex:none;margin-top:5px}
.foot-brand{left:500px;top:60px;width:200px;text-align:center}
.foot-brand .brand-mark{width:86px;height:86px;margin:0 auto 12px}
.foot-brand .brand-name{color:var(--white)}
.socials{display:flex;justify-content:center;gap:12px;margin-top:18px}
.socials i{width:30px;height:30px;border-radius:50%;background:var(--white)}
.copy{margin-top:22px;font:400 10px "Poppins",sans-serif;color:#8b8b8b}
</style>
</head>
<body>

<header class="section site-header">
  <nav class="abs main-nav"><span class="active">Home</span><span>About Us</span><span>Services</span><span>Contact Us</span></nav>
  <div class="abs brand"><span class="brand-mark"></span><span class="brand-name">Crestline Floors</span></div>
  <div class="abs call">
    <span class="call-icon"><svg width="14" height="14" viewBox="0 0 24 24" fill="#fff"><path d="M6.6 10.8a15 15 0 0 0 6.6 6.6l2.2-2.2c.3-.3.7-.4 1-.2 1.1.4 2.3.6 3.6.6.6 0 1 .4 1 1V20c0 .6-.4 1-1 1C10.6 21 3 13.4 3 4c0-.6.4-1 1-1h3.5c.6 0 1 .4 1 1 0 1.3.2 2.5.6 3.6.1.3 0 .7-.2 1z"/></svg></span>
    <span class="call-text"><small>Call Us</small><b>(209) 555-0142</b></span>
  </div>
  <span class="btn">Free Consultation</span>
</header>

<section class="section hero">
  <div class="photo" style="inset:0" role="img" aria-label="Modern office interior with glass walls, city view and polished wood floor"></div>
  <div class="abs hero-dots"><i></i><i></i><i></i></div>
  <h1 class="abs hero-title">We Provide Ultimate<br>Commercial Flooring Services.</h1>
  <div class="abs hero-list"><span>CARPET</span><span>WOOD</span><span>TILE</span><span>LAMINATE</span><span>VINYL</span></div>
  <span class="btn">Free Consultation</span>
</section>

<section class="section about">
  <div class="abs about-ring"></div>
  <div class="abs about-photo" role="img" aria-label="Workers installing a wooden floor in a bright room"></div>
  <div class="abs about-badge">Crestline<br>Floors</div>
  <div class="abs about-copy">
    <h2 class="h2">We Provide The Best<br>Commercial Flooring Services</h2>
    <p class="p">We are Crestline, a flooring team serving schools, hospitals and public buildings across California. Lorem ipsum has been the industry standard dummy text ever since the 1500s, when an unknown printer took a galley of type and scrambled it to make a type specimen book. It has survived not only five centuries but also the leap into electronic typesetting.</p>
    <ul class="ticks">
      <li>We are licensed and insured crews</li><li>Trusted quality in our work</li>
      <li>We're happy to help with your plan</li><li>Optimising the value of a project</li>
      <li>We have the latest technologies</li><li>Proven care in type and finish</li>
    </ul>
    <span class="btn">More About Us</span>
  </div>
</section>

<section class="section services">
  <div class="abs section-head"><h2 class="h2">We Provide Flooring Services</h2><p>To many clients like government, homes and offices</p></div>

  <div class="photo" style="left:144px;top:160px;width:216px;height:216px;background:linear-gradient(160deg,#caa27a,#8c5b36)" role="img" aria-label="Empty room with wood floor"></div>
  <div class="tile-label" style="left:144px;top:388px;width:216px">Wood</div>

  <div class="photo" style="left:400px;top:160px;width:392px;height:400px;background:linear-gradient(170deg,#d6cbbd,#a5703f 55%,#6e4424)" role="img" aria-label="Worker applying coating to a parquet floor"></div>
  <div class="tile-label" style="left:400px;top:580px;width:392px">Coatings</div>
  <p class="coat-text">Lorem ipsum has been the industry standard dummy text ever since the 1500s, when an unknown printer took a galley of type.</p>

  <div class="photo" style="left:840px;top:160px;width:216px;height:216px;background:linear-gradient(160deg,#7f8a93,#4b545b)" role="img" aria-label="Hands spreading overlay compound with a trowel"></div>
  <div class="tile-label" style="left:840px;top:388px;width:216px">Overlays</div>

  <div class="photo" style="left:144px;top:432px;width:216px;height:216px;background:linear-gradient(160deg,#d9d9d6,#a8a8a4)" role="img" aria-label="Polished concrete floor close up"></div>
  <div class="tile-label" style="left:144px;top:660px;width:216px">Concrete</div>

  <div class="photo" style="left:840px;top:432px;width:216px;height:216px;background:linear-gradient(160deg,#f0f0f0,#b9bec2)" role="img" aria-label="Bright hall with large tiled floor"></div>
  <div class="tile-label" style="left:840px;top:660px;width:216px">Tile</div>

  <div class="photo" style="left:144px;top:712px;width:256px;height:236px;background:linear-gradient(160deg,#9aa0a3,#5d6064)" role="img" aria-label="Office lounge with resilient flooring"></div>
  <div class="tile-label" style="left:144px;top:960px;width:256px">Resilient</div>

  <div class="photo" style="left:416px;top:712px;width:328px;height:236px;background:linear-gradient(160deg,#8f8f8b,#c9a06a 60%,#6b6b66)" role="img" aria-label="Office with patterned carpet tiles and orange seating"></div>
  <div class="tile-label" style="left:416px;top:960px;width:328px">Carpet</div>

  <div class="photo" style="left:760px;top:712px;width:296px;height:236px;background:linear-gradient(160deg,#cfd8de,#7d8e99)" role="img" aria-label="Worker using a floor machine on a self-leveling surface"></div>
  <div class="tile-label" style="left:760px;top:960px;width:296px">Vapor Control &amp; Self-Leveling</div>
</section>

<section class="section banner" role="img" aria-label="Dark wood plank floor background">
  <h3>What kind of design projects are you interested in?</h3>
  <p>Send us a short project summary. We will reply with a plan, price and schedule.</p>
  <span class="btn">Free Consultation</span>
</section>

<section class="section projects">
  <h2 class="h2">Explore Our Flooring Projects</h2>
  <span class="btn">All Projects</span>
  <div class="photo" style="left:144px;top:160px;width:440px;height:320px;background:linear-gradient(170deg,#e6e6e4,#b79c7e 60%,#8f7356)" role="img" aria-label="Open office with solid wood flooring"></div>
  <div class="photo" style="left:608px;top:160px;width:448px;height:320px;background:linear-gradient(170deg,#f4f4f2,#cfc8bf 60%,#a2988b)" role="img" aria-label="Lounge room with laminate flooring and dark sofa"></div>
  <div class="abs proj-arrow"><svg width="14" height="14" viewBox="0 0 24 24" fill="none" stroke="#fff" stroke-width="3"><path d="M15 5l-7 7 7 7"/></svg></div>
  <div class="proj-label" style="left:144px">Solid Wood Flooring</div>
  <div class="proj-label" style="left:608px">Laminate Flooring</div>
</section>

<section class="section testimonials">
  <div class="abs testi-copy">
    <h2 class="h2">Here's What Our Satisfied<br>Clients Are Saying</h2>
    <div class="quote">“</div>
    <p class="p">These are the most beautiful cabinets! So well made. The contractor installing them said they're some of the best he's ever seen. Everyone that sees them wants to know where I bought them.</p>
    <div class="person"><span class="avatar" role="img" aria-label="Client portrait"></span><span><b>Marla Quentin</b><small>Facility Manager</small></span></div>
  </div>
  <div class="photo testi-photo" role="img" aria-label="Executive office with checkered carpet tiles"></div>
</section>

<section class="section areas">
  <div class="photo map" role="img" aria-label="Map of California with the served counties highlighted in red"></div>
  <div class="abs areas-copy">
    <h2 class="h2">Areas We Serve</h2>
    <p class="p">Lorem ipsum has been the industry standard dummy text ever since the 1500s, when an unknown printer took a galley of type.</p>
    <div class="area-list">
      <div class="area-item"><span class="area-thumb"></span><span><b>418 Alder Row</b><small>Lodi, CA</small></span></div>
      <div class="area-item"><span class="area-thumb"></span><span><b>Pinecrest</b><small>Tuolumne County</small></span></div>
      <div class="area-item"><span class="area-thumb"></span><span><b>Willow Bend</b><small>San Joaquin County</small></span></div>
      <div class="area-item"><span class="area-thumb"></span><span><b>Willow Bend</b><small>Stanislaus County</small></span></div>
    </div>
  </div>
</section>

<section class="section contact">
  <div class="photo" style="inset:0" role="img" aria-label="Workers sanding and fitting a parquet floor in a sunlit room"></div>
  <form class="abs contact-card">
    <h3>Get In Touch</h3>
    <p class="lead">Tell us about your floor and the size of the site. We reply within one business day with next steps.</p>
    <div class="field-row"><div class="field">Name</div><div class="field">Email address</div></div>
    <div class="field-row"><div class="field">Select your service <span>▾</span></div></div>
    <div class="field-row"><div class="field">Subject</div></div>
    <div class="field-row"><div class="field tall">Message</div></div>
    <span class="btn">Submit Now</span>
  </form>
</section>

<footer class="section site-footer">
  <div class="foot-col" style="left:144px">
    <h4>Contact Details</h4>
    <ul>
      <li><i></i>1200 Harbor Way,<br>Stockton, CA</li>
      <li><i></i>(209) 555-0142</li>
      <li><i></i>hello@crestlinefloors.co</li>
    </ul>
  </div>
  <div class="abs foot-brand">
    <div class="brand-mark"></div>
    <div class="brand-name">Crestline Floors</div>
    <div class="socials"><i></i><i></i><i></i></div>
    <div class="copy">© 2024 Crestline Floors. All Rights Reserved</div>
  </div>
  <div class="foot-col" style="left:844px">
    <h4>Our Links</h4>
    <ul>
      <li>Home</li><li>About Us</li><li>Services</li><li>Our Approach</li><li>Projects</li><li>Team</li><li>Contact Us</li>
    </ul>
  </div>
</footer>

</body>
</html>
```